Informational Site for Advanced Chemistry R&D

The company develops oxidation chemistry for air, water, fuel pollution controls. The site has been prototyped at www.velmirlab.net. Take a look. Now, the task is to design it for eye-catching beauty with use of color, on-page scroll-driven color transition and parallax effects. Should capture the themes: high technology, wow it's beautiful, modern, uncluttered, clean urban environment.

Target Market(s)

China Environmentally Conscious Government and Industry,

Industry/Entity Type

It Company

Number of Pages Required

3 page

Font styles to use
Sans Serif

Requirements
Must have
• Parallax effects, desktop compatible, Rich, Modern, Simple, Graphic
Nice to have
• Mobile Phone Compatible
Should not have
• Flash, or anything that is slow to load or requires high bandwidth

```html
<!DOCTYPE html>
<html lang="en">
<head>
<meta charset="utf-8">
<title>VelmirLab — Advanced Oxidation Science</title>
<link rel="stylesheet" href="https://fonts.googleapis.com/css2?family=Montserrat:wght@300;400;600;700&display=swap">
<style>
:root{
  --blue:#1f78c8;
  --blue-deep:#1565b8;
  --blue-light:#3a92dc;
  --teal:#27a39b;
  --teal-deep:#1f8f8c;
  --teal-light:#5cc3bd;
  --frame:#8fc6d9;
  --white:#ffffff;
}
*{margin:0;padding:0;box-sizing:border-box}
html,body{width:1200px;height:2353px;overflow:hidden;background:var(--white)}
body{position:relative;font-family:"Montserrat",Arial,sans-serif;color:var(--teal)}
.abs{position:absolute}
.backdrop{position:absolute;left:0;top:0}

/* navigation */
.nav{position:absolute;left:0;width:1200px;height:82px}
.brand{position:absolute;left:262px;top:30px;display:flex;align-items:center;gap:7px;color:var(--white);font-weight:600;font-size:14px}
.brand-dot{width:10px;height:10px;border-radius:50%;background:var(--white)}
.menu{position:absolute;top:40px;display:flex;list-style:none}
.menu li{position:absolute;white-space:nowrap;color:var(--white);font-size:9px;font-weight:700;letter-spacing:.14em}
.social{position:absolute;top:42px}
.social span{position:absolute;width:7px;height:7px;border-radius:50%;background:var(--white)}

/* common type */
.eyebrow{position:absolute;font-size:10px;font-weight:600;letter-spacing:.16em;display:flex;align-items:center;gap:12px}
.eyebrow .rule{display:inline-block;width:42px;height:1px;background:currentColor}
.headline{position:absolute;font-size:28px;font-weight:300;letter-spacing:.16em;line-height:41px;text-transform:uppercase}
.headline b{font-weight:700}
.btn{position:absolute;width:181px;height:39px;border:2px solid currentColor;border-radius:20px;font-size:9px;font-weight:700;letter-spacing:.16em;display:flex;align-items:center;justify-content:center}
.vertical{position:absolute;writing-mode:vertical-rl;font-size:9px;font-weight:700;letter-spacing:.18em;color:var(--white);display:flex;align-items:center;gap:14px}
.vertical .rule{display:inline-block;width:1px;height:48px;background:var(--white)}

/* hero */
.hero-text{color:var(--white)}

/* applications */
.app-photo{position:absolute;width:310px;height:203px}
.app-frame{position:absolute;width:308px;height:204px;border:2px solid var(--frame)}
.app-label{position:absolute;text-transform:uppercase}
.app-for{font-size:27px;font-weight:300;letter-spacing:.14em;display:flex;align-items:center;gap:14px}
.app-for .rule{display:inline-block;width:40px;height:1px;background:currentColor}
.app-name{font-size:27px;font-weight:700;letter-spacing:.14em;line-height:41px;margin-top:6px}
.app-bar{width:46px;height:4px;background:currentColor;margin-top:8px}
.right .app-for{justify-content:flex-end;flex-direction:row}
.right{text-align:right}
.right .app-bar{margin-left:auto}
.teal{color:var(--teal)}
.blue{color:var(--blue-deep)}
</style>
</head>
<body>

<!-- background bands -->
<svg class="backdrop" width="1200" height="2353" viewBox="0 0 1200 2353" aria-hidden="false">
  <defs>
    <linearGradient id="waterTone" x1="0" y1="0" x2="1" y2="1">
      <stop offset="0" stop-color="#2a7fcd"/>
      <stop offset=".5" stop-color="#1d72c2"/>
      <stop offset="1" stop-color="#2b86d2"/>
    </linearGradient>
    <linearGradient id="cityTone" x1="0" y1="0" x2="0" y2="1">
      <stop offset="0" stop-color="#28a3a0"/>
      <stop offset=".55" stop-color="#3cb0aa"/>
      <stop offset=".8" stop-color="#2f9f9a"/>
      <stop offset="1" stop-color="#1f8f8c"/>
    </linearGradient>
  </defs>
  <polygon points="0,0 1200,0 1200,604 0,420" fill="url(#waterTone)" role="img" aria-label="Rippling blue water surface"/>
  <polygon points="0,925 1200,737 1200,1346 0,1346" fill="url(#cityTone)" role="img" aria-label="City skyline reflected in a river under a teal tint"/>
  <rect x="0" y="2271" width="1200" height="82" fill="url(#waterTone)" role="img" aria-label="Rippling blue water surface"/>
  <circle cx="598" cy="471" r="12" fill="none" stroke="#8fc6d9" stroke-width="1.5"/>
  <polyline points="593,469 598,474 603,469" fill="none" stroke="#8fc6d9" stroke-width="1.5"/>
</svg>

<!-- header -->
<header class="nav" style="top:0">
  <div class="brand"><span class="brand-dot"></span>VelmirLab</div>
  <ul class="menu">
    <li style="left:431px">HOME</li>
    <li style="left:501px">WATER</li>
    <li style="left:574px">DIESEL</li>
    <li style="left:651px">COAL</li>
    <li style="left:718px">VOC</li>
    <li style="left:778px">ABOUT</li>
  </ul>
  <div class="social"><span style="left:898px"></span><span style="left:922px"></span><span style="left:945px"></span></div>
</header>

<!-- hero -->
<section class="hero-text">
  <div class="eyebrow" style="left:271px;top:145px;color:var(--white)"><span class="rule"></span>VELMIRLAB</div>
  <h1 class="headline" style="left:267px;top:168px;color:var(--white)">Advanced <b>Oxidation</b><br>Science for Environmental<br>Pollution Management</h1>
  <div class="btn" style="left:271px;top:320px;color:var(--white)">EXPLORE</div>
  <div class="vertical" style="left:942px;top:157px">VELMIRLAB<span class="rule"></span>WATER</div>
</section>

<!-- free radical -->
<section>
  <div class="eyebrow" style="left:243px;top:567px;color:var(--teal)">FREE RADICAL<span class="rule"></span></div>
  <h2 class="headline" style="left:241px;top:590px;color:var(--teal);font-size:29px">Environmental Pollution<br>Control Solutions Employing<br>Nature's Mostreactive <b>Free Radical</b></h2>
  <div class="btn" style="left:240px;top:742px;color:var(--teal)">EXPLORE</div>
</section>

<!-- clean urban -->
<section>
  <div class="eyebrow" style="left:362px;top:1031px;color:var(--white)"><span class="rule"></span>CLEAN URBAN</div>
  <h2 class="headline" style="left:359px;top:1055px;color:var(--white)">Feel the <b>Clean Air</b><br>in your city<br>everyday</h2>
  <div class="vertical" style="left:824px;top:1016px">CLEAN<span class="rule"></span>FRESH AIR</div>
</section>

<!-- applications -->
<section>
  <div class="app-frame" style="left:221px;top:1290px"></div>
  <div class="app-photo" role="img" aria-label="Circular wastewater clarifier tank with trees behind" style="left:234px;top:1282px;background:linear-gradient(180deg,#6f9a5a 0%,#4d7f48 22%,#1d4a78 40%,#2a5f8e 75%,#9aa7b0 100%)"></div>
  <div class="app-label teal" style="left:560px;top:1374px">
    <div class="app-for"><span class="rule"></span>For</div>
    <div class="app-name" style="margin-left:54px">Wastewater</div>
    <div class="app-bar" style="margin-left:56px;margin-top:2px"></div>
  </div>

  <div class="app-frame" style="left:670px;top:1511px"></div>
  <div class="app-photo" role="img" aria-label="Row of white cylindrical diesel storage tanks under blue sky" style="left:656px;top:1522px;background:linear-gradient(180deg,#1f4f9e 0%,#3a6fb8 40%,#e6e8ea 55%,#c9ccd0 80%,#6b6a5e 100%)"></div>
  <div class="app-label blue right" style="left:290px;top:1590px;width:350px">
    <div class="app-for">For<span class="rule"></span></div>
    <div class="app-name" style="margin-right:64px">Diesel Fuel</div>
    <div class="app-bar" style="margin-right:66px;margin-top:2px"></div>
  </div>

  <div class="app-frame" style="left:221px;top:1756px"></div>
  <div class="app-photo" role="img" aria-label="Industrial flue gas treatment towers and pipework" style="left:234px;top:1768px;background:linear-gradient(180deg,#dcdcdc 0%,#c8cbcf 45%,#5b7390 70%,#2d4766 100%)"></div>
  <div class="app-label teal" style="left:560px;top:1832px">
    <div class="app-for"><span class="rule"></span>For</div>
    <div class="app-name" style="margin-left:54px">Coal Flue Gas</div>
    <div class="app-bar" style="margin-left:56px;margin-top:2px"></div>
  </div>

  <div class="app-frame" style="left:670px;top:1997px"></div>
  <div class="app-photo" role="img" aria-label="Smokestacks releasing emissions against a sunset sky" style="left:656px;top:2009px;background:linear-gradient(180deg,#2b2f3a 0%,#5a5560 35%,#c27a45 62%,#e39a4a 72%,#1c1a1a 85%,#0e0e0e 100%)"></div>
  <div class="app-label blue right" style="left:290px;top:2078px;width:350px">
    <div class="app-for">For<span class="rule"></span></div>
    <div class="app-name" style="margin-right:64px">Volatile<br>Organics</div>
    <div class="app-bar" style="margin-right:66px;margin-top:2px"></div>
  </div>
</section>

<!-- footer -->
<footer class="nav" style="top:2271px">
  <div class="brand" style="top:30px"><span class="brand-dot"></span>VelmirLab</div>
  <ul class="menu">
    <li style="left:431px">HOME</li>
    <li style="left:501px">WATER</li>
    <li style="left:574px">DIESEL</li>
    <li style="left:651px">COAL</li>
    <li style="left:718px">VOC</li>
    <li style="left:778px">ABOUT</li>
  </ul>
  <div class="social"><span style="left:898px"></span><span style="left:922px"></span><span style="left:945px"></span></div>
</footer>

</body>
</html>
```